Flyerdesign for a Sports Homepage

I need a design for our Merchandise/Discount Flyer.
we are going to sell high class sports equipment.
the flyer should be in Size A5 or between A5 and A4.
there should be mentioned our Product names:
Product name for powerlifting: Torvik
Product name for Boxing: ZL Boxing
Product name for Martial Arts: Murelt
Product name for MMA: PitVolt
Product name for Bodybuilding: Bramfold

our Storename: PushAndDuel
Homepage: www.pushandduel.example

there should be space for entering a discount code
shop logo and brand logos: all pictures are attached.

out of the box thinking is welcome

Target Market(s)

People who do powersports like powerlifting or mma

Industry/Entity Type

Sport

Requirements
Must have
• 2 sides, all our brandnames, homepage, shop name and sports

```html
<!DOCTYPE html>
<html lang="en">
<head>
<meta charset="utf-8">
<title>Push And Duel – Merchandise Flyer</title>
<link rel="stylesheet" href="https://fonts.googleapis.com/css2?family=Oswald:wght@500;600&family=Montserrat:wght@600&display=swap">
<style>
  :root {
    --stage: #d4d4d4;
    --black: #050507;
    --charcoal: #1a1a1a;
    --gold-deep: #a27a3c;
    --gold-mid: #d2b470;
    --gold-light: #f3e9a6;
    --gold-text: #d8bf7f;
    --gold-label: #e8d395;
    --field: #b9a36a;
    --red: #e3202b;
    --heading: #17130c;
  }
  * { box-sizing: border-box; margin: 0; padding: 0; }
  html, body { width: 1200px; height: 960px; overflow: hidden; }
  body { background: var(--stage); position: relative; font-family: "Oswald", "Arial Narrow", sans-serif; }

  .page { position: absolute; top: 128px; width: 524px; height: 726px; overflow: hidden; background: var(--black); }
  .page--front { left: 58px; }
  .page--back { left: 619px; width: 514px; }
  .page__art { position: absolute; inset: 0; width: 100%; height: 100%; }

  /* Front */
  .brand-frame {
    position: absolute; left: 102px; top: 4px; width: 321px; height: 212px;
    border: 3px solid var(--gold-mid);
    background: linear-gradient(160deg, #2b2b2b, #151515 70%);
    display: flex; align-items: center; justify-content: center; gap: 12px;
  }
  .brand-frame__square { width: 18px; height: 18px; background: var(--gold-mid); }
  .brand-frame__name {
    font-family: "Montserrat", sans-serif; font-weight: 600; font-size: 21px;
    letter-spacing: 4px; color: var(--gold-mid);
  }

  .field-label {
    position: absolute; color: var(--heading); font-weight: 600; font-size: 23px;
    line-height: 1; text-transform: uppercase;
  }
  .field-label--store { left: 7px; top: 496px; }
  .field-label--home { left: 10px; top: 594px; }

  .tag {
    position: absolute; background: var(--red);
    clip-path: polygon(0 0, 100% 0, calc(100% - 14px) 100%, 0 100%);
  }
  .tag__body {
    display: flex; align-items: center; height: 100%;
    background: var(--black); color: var(--gold-label);
    clip-path: polygon(0 0, calc(100% - 6px) 0, calc(100% - 20px) 100%, 0 100%);
    font-weight: 500; white-space: nowrap;
  }
  .tag--store { left: 8px; top: 527px; width: 180px; height: 30px; }
  .tag--store .tag__body { padding-left: 16px; font-size: 19px; }
  .tag--url { left: 6px; top: 625px; width: 180px; height: 31px; }
  .tag--url .tag__body { padding-left: 5px; font-size: 12.5px; letter-spacing: 0.2px; font-weight: 600; }

  .discount__label {
    position: absolute; left: 340px; top: 634px; font-size: 24px; font-weight: 500;
    color: var(--gold-text); line-height: 1;
  }
  .discount__field {
    position: absolute; left: 339px; top: 668px; width: 171px; height: 30px;
    border-radius: 12px; background: var(--field);
  }

  /* Back */
  .product-heading {
    position: absolute; left: 14px; top: 17px; width: 110px;
    color: var(--gold-text); font-weight: 500; font-size: 25px; line-height: 31px;
    text-transform: uppercase;
  }
  .tag--product { height: 36px; }
  .tag--product .tag__body { padding-left: 22px; font-size: 26px; }
  .tag--torvik { left: 321px; top: 105px; width: 134px; }
  .tag--zl { left: 294px; top: 235px; width: 166px; }
  .tag--murelt { left: 271px; top: 363px; width: 145px; }
  .tag--pitvolt { left: 244px; top: 498px; width: 177px; }
  .tag--bramfold { left: 216px; top: 642px; width: 175px; }
</style>
</head>
<body>

<section class="page page--front" aria-label="Flyer front">
  <svg class="page__art" viewBox="0 0 941 1305" preserveAspectRatio="none" aria-hidden="true">
    <defs>
      <linearGradient id="goldFront" x1="0" y1="0" x2="1" y2="0">
        <stop offset="0" stop-color="#a27a3c"/>
        <stop offset="0.3" stop-color="#d2b470"/>
        <stop offset="0.6" stop-color="#f3e9a6"/>
        <stop offset="0.85" stop-color="#d0ae68"/>
        <stop offset="1" stop-color="#a27a3c"/>
      </linearGradient>
    </defs>
    <rect width="941" height="1305" fill="#050507"/>
    <polygon points="0,730 941,350 941,385 0,765" fill="#c5a867"/>
    <polygon points="0,810 941,425 941,443 0,827" fill="#ffffff"/>
    <polygon points="0,827 941,443 941,1005 217,1235 0,1220" fill="url(#goldFront)"/>
    <polygon points="0,1220 217,1235 941,1305 0,1305" fill="#1a1a1a"/>
  </svg>

  <div class="brand-frame">
    <span class="brand-frame__square"></span>
    <span class="brand-frame__name">PUSH AND DUEL</span>
  </div>

  <h2 class="field-label field-label--store">Our store name:</h2>
  <div class="tag tag--store"><div class="tag__body">Push And Duel</div></div>

  <h2 class="field-label field-label--home">Homepage:</h2>
  <div class="tag tag--url"><div class="tag__body">www.pushandduel.example</div></div>

  <p class="discount__label">DISCOUNT CODE</p>
  <div class="discount__field" aria-label="Discount code field"></div>
</section>

<section class="page page--back" aria-label="Flyer back">
  <svg class="page__art" viewBox="0 0 924 1305" preserveAspectRatio="none">
    <defs>
      <linearGradient id="goldBack" x1="0" y1="0" x2="1" y2="0">
        <stop offset="0" stop-color="#d2b470"/>
        <stop offset="0.55" stop-color="#f3e9a6"/>
        <stop offset="0.85" stop-color="#d0ae68"/>
        <stop offset="1" stop-color="#a27a3c"/>
      </linearGradient>
      <radialGradient id="fire" cx="0.55" cy="0.5" r="0.6">
        <stop offset="0" stop-color="#f0841e"/>
        <stop offset="0.45" stop-color="#b5220f"/>
        <stop offset="1" stop-color="#2a0606"/>
      </radialGradient>
    </defs>
    <rect width="924" height="1305" fill="url(#goldBack)"/>
    <rect x="0" y="1277" width="924" height="18" fill="#050507"/>
    <polygon points="0,0 623,0 378,1305 0,1305" fill="#050507"/>
    <line x1="250" y1="0" x2="0" y2="995" stroke="#c5a867" stroke-width="5"/>

    <polygon role="img" aria-label="Powerlifting artwork for Torvik" points="250,0 623,0 562,325 206,175" fill="url(#fire)"/>
    <polygon role="img" aria-label="Boxing ring artwork for ZL Boxing" points="206,175 562,325 516,570 149,400" fill="url(#fire)"/>
    <polygon role="img" aria-label="Martial arts artwork for Murelt" points="149,400 516,570 472,805 93,625" fill="url(#fire)"/>
    <polygon role="img" aria-label="MMA cage artwork for PitVolt" points="93,625 472,805 429,1035 0,995" fill="url(#fire)"/>
    <polygon role="img" aria-label="Bodybuilding artwork for Bramfold" points="0,1012 426,1052 378,1305 0,1305" fill="url(#fire)"/>

    <g stroke="#e3202b" stroke-width="4">
      <line x1="206" y1="175" x2="562" y2="325"/>
      <line x1="149" y1="400" x2="516" y2="570"/>
      <line x1="93" y1="625" x2="472" y2="805"/>
      <line x1="0" y1="995" x2="429" y2="1035"/>
    </g>
  </svg>

  <h2 class="product-heading">Our product names</h2>

  <div class="tag tag--product tag--torvik"><div class="tag__body">TORVIK</div></div>
  <div class="tag tag--product tag--zl"><div class="tag__body">ZL BOXING</div></div>
  <div class="tag tag--product tag--murelt"><div class="tag__body">MURELT</div></div>
  <div class="tag tag--product tag--pitvolt"><div class="tag__body">PITVOLT</div></div>
  <div class="tag tag--product tag--bramfold"><div class="tag__body">BRAMFOLD</div></div>
</section>

</body>
</html>
```